I need a box design created for a DNA Fitness Test

I need a modern and sleek box design for a fitness test. The box needs to have our logo on it and should be clean and modern. The Box is 9 Inches Long 3 and 3/4 inches wide, and 2 inches tall. Company logo attached. The company name is cedar vitality.

Target Market(s)

Fitness

Industry/Entity Type

Fitness

Requirements
Must have
• Our logo

```html
<!DOCTYPE html>
<html lang="en">
<head>
<meta charset="utf-8">
<title>Cedar Vitality – DNA Fitness Test box</title>
<link rel="stylesheet" href="https://fonts.googleapis.com/css2?family=Montserrat:wght@800&family=Open+Sans:wght@300&display=swap">
<style>
  :root {
    --bg: #031a04;
    --blue-deep: #2a6fbf;
    --blue-mid: #4d9fdc;
    --cyan: #6ccaee;
    --sky-light: #dcedf8;
    --paper: #f4f7fa;
    --ink: #0b0b0b;
    --white: #ffffff;
  }
  * { box-sizing: border-box; margin: 0; padding: 0; }
  html, body { width: 1200px; height: 914px; overflow: hidden; }
  body {
    background: var(--bg);
    position: relative;
    font-family: "Open Sans", sans-serif;
  }
  .panel { position: absolute; overflow: hidden; }

  /* Top face: 9in × 3.75in */
  .top-face {
    left: 150px; top: 60px; width: 900px; height: 375px;
    background: linear-gradient(100deg, var(--blue-deep) 0%, var(--blue-mid) 22%, #9fd5f2 50%, var(--sky-light) 80%, #eef6fb 100%);
  }
  .helix-art {
    position: absolute; left: 150px; top: 0; width: 260px; height: 375px;
    background: linear-gradient(90deg, rgba(255,255,255,0) 0%, rgba(255,255,255,0.35) 50%, rgba(255,255,255,0) 100%);
  }
  .brand {
    position: absolute; display: flex; align-items: center; gap: 12px;
    font-family: "Montserrat", sans-serif; font-weight: 800; color: var(--ink);
    text-transform: uppercase; white-space: nowrap;
  }
  .brand-dot { border-radius: 50%; background: var(--blue-deep); flex: none; }
  .top-face .brand { right: 90px; top: 160px; font-size: 36px; letter-spacing: 1px; }
  .top-face .brand-dot { width: 34px; height: 34px; }

  /* Front face: 9in × 2in */
  .front-face {
    left: 150px; top: 455px; width: 900px; height: 200px;
    background: linear-gradient(90deg, var(--paper) 0%, var(--sky-light) 25%, var(--cyan) 50%, var(--blue-mid) 72%, var(--blue-deep) 100%);
  }
  .product-title {
    position: absolute; left: 560px; top: 28px; color: var(--white); font-weight: 300;
  }
  .product-title .dna { font-size: 92px; line-height: 1; letter-spacing: 34px; }
  .product-title .test { font-size: 30px; letter-spacing: 1px; margin-top: 4px; }

  /* End face: 3.75in × 2in */
  .end-face {
    left: 150px; top: 675px; width: 375px; height: 200px;
    background: linear-gradient(90deg, var(--paper) 0%, #e8f2f8 60%, var(--sky-light) 100%);
  }
  .molecule-art {
    position: absolute; inset: 0;
    background: radial-gradient(ellipse at 70% 60%, rgba(170,205,228,0.45), rgba(255,255,255,0) 70%);
  }
  .end-face .brand { left: 90px; top: 82px; font-size: 22px; }
  .end-face .brand-dot { width: 20px; height: 20px; }
</style>
</head>
<body>
  <section class="panel top-face" aria-label="Box lid">
    <div class="helix-art" role="img" aria-label="Glowing DNA double helix with drifting particles"></div>
    <div class="brand"><span class="brand-dot"></span>Cedar Vitality</div>
  </section>

  <section class="panel front-face" aria-label="Box front">
    <div class="product-title">
      <div class="dna">DNA</div>
      <div class="test">FITNESS TEST</div>
    </div>
  </section>

  <section class="panel end-face" aria-label="Box end">
    <div class="molecule-art" role="img" aria-label="Faint molecular network and helix pattern"></div>
    <div class="brand"><span class="brand-dot"></span>Cedar Vitality</div>
  </section>
</body>
</html>
```